Business Card Design

I am an Event and Wedding Planner in need of an eye catching business card featuring my logo (attached), my contact details, and my company tagline (Making each one of your gatherings radiant...) I would like the tagline in font similar the logo's font.
Updates
I have just noticed that my logo has a misspelling so for the final design, I will be uploading a corrected logo as soon as I have it.
My apologies.
Reason: Waiting on a corrected logo...Occasions is misspelled and it should say Weddings not Wedding
The logo has been corrected so now Occasions is spelled correctly and it says Weddings instead of Wedding. Please use Edwardian Script ITC as the font for the tagline so it will match the logo. Thank you for your patience.
Target Market(s)
Engaged couples and people hosting milestone celebrations. 25-50 years old, predominately female
Industry/Entity Type
Business
Contact Information for Business Card
Delphine Marsh, Event Manager / Owner, Mobile: 0491 836 254, Email: delphine@radiantgatheringsco.com.au, www.radiantgatheringsco.com.au, Making each one of your gatherings radiant...

```html
<!DOCTYPE html>
<html lang="en">
<head>
<meta charset="utf-8">
<title>Radiant Gatherings Co — Business Card</title>
<link href="https://fonts.googleapis.com/css2?family=Montserrat:wght@300;400&family=Pinyon+Script&display=swap" rel="stylesheet">
<style>
  :root {
    --backdrop: #cfcfcf;
    --card: #3a3a3a;
    --ink: #f2f2f2;
    --ink-soft: #cfcfcf;
    --strip: #ffffff;
    --rule: #bdbdbd;
    --ornament: rgba(225, 225, 225, 0.30);
    --ornament-fade: rgba(225, 225, 225, 0);
  }
  * { box-sizing: border-box; margin: 0; padding: 0; }
  html, body {
    width: 1200px; height: 900px; overflow: hidden;
    background: var(--backdrop);
    font-family: "Montserrat", sans-serif;
  }
  .canvas { position: relative; width: 1200px; height: 900px; }
  .card {
    position: absolute; left: 340px; width: 520px; height: 300px;
    background: var(--card);
    box-shadow: 0 10px 28px rgba(0,0,0,0.28);
    overflow: hidden;
  }
  .card--back { top: 110px; }
  .card--front { top: 470px; }

  /* back side */
  .side-strip {
    position: absolute; left: 0; top: 0; bottom: 0; width: 70px;
    background: var(--strip);
  }
  .identity {
    position: absolute; right: 36px; top: 38px; text-align: right; color: var(--ink);
  }
  .identity__name { font-weight: 300; font-size: 24px; letter-spacing: 3px; }
  .identity__role {
    font-weight: 300; font-size: 9px; letter-spacing: 0.5px; color: var(--ink-soft); margin-top: 4px;
  }
  .contact {
    position: absolute; left: 130px; top: 170px; list-style: none; color: var(--ink);
    font-weight: 300; font-size: 12.5px;
  }
  .contact li { display: flex; align-items: center; gap: 10px; margin-bottom: 9px; }
  .contact svg { width: 11px; height: 11px; flex: none; }

  /* front side */
  .ornament-band {
    position: absolute; left: 30px; right: 30px; top: 24px; height: 44px;
    background: linear-gradient(90deg, var(--ornament-fade), var(--ornament) 25%, var(--ornament) 75%, var(--ornament-fade));
  }
  .brand {
    position: absolute; left: 0; right: 0; top: 100px; text-align: center;
    color: var(--ink); font-weight: 300; font-size: 26px; letter-spacing: 4px;
  }
  .rule { position: absolute; height: 1px; background: var(--rule); }
  .rule--under-brand { left: 150px; right: 150px; top: 150px; }
  .divider-mark {
    position: absolute; left: 252px; top: 168px; width: 16px; height: 8px;
  }
  .tagline {
    position: absolute; left: 0; right: 0; top: 190px; text-align: center;
    font-family: "Pinyon Script", cursive; font-size: 27px; color: var(--ink);
  }
  .rule--lower { left: 110px; right: 110px; top: 250px; }
</style>
</head>
<body>
<main class="canvas">
  <section class="card card--back" aria-label="Business card back">
    <div class="side-strip"></div>
    <div class="identity">
      <p class="identity__name">Delphine Marsh</p>
      <p class="identity__role">Event Manager / Owner</p>
    </div>
    <ul class="contact">
      <li>
        <svg viewBox="0 0 12 12" aria-hidden="true"><path d="M2.5 1 L4.5 1 L5 3.5 L3.8 4.4 Q5 7 7.6 8.2 L8.5 7 L11 7.5 L11 9.5 Q11 11 9.5 11 Q1 10 1 2.5 Q1 1 2.5 1 Z" fill="#f2f2f2"/></svg>
        0491 836 254
      </li>
      <li>
        <svg viewBox="0 0 12 12" aria-hidden="true"><rect x="0.5" y="2" width="11" height="8" fill="#f2f2f2"/><path d="M0.5 2 L6 6.5 L11.5 2" fill="none" stroke="#3a3a3a" stroke-width="1"/></svg>
        delphine@radiantgatheringsco.com.au
      </li>
      <li>
        <svg viewBox="0 0 12 12" aria-hidden="true"><circle cx="6" cy="6" r="5" fill="none" stroke="#f2f2f2" stroke-width="1.2"/><ellipse cx="6" cy="6" rx="2.2" ry="5" fill="none" stroke="#f2f2f2" stroke-width="1"/><path d="M1 6 H11" stroke="#f2f2f2" stroke-width="1"/></svg>
        www.radiantgatheringsco.com.au
      </li>
    </ul>
  </section>

  <section class="card card--front" aria-label="Business card front">
    <div class="ornament-band" role="img" aria-label="Decorative scrolling floral vine border across the top of the card"></div>
    <p class="brand">Radiant Gatherings Co</p>
    <div class="rule rule--under-brand"></div>
    <svg class="divider-mark" viewBox="0 0 16 8" aria-hidden="true">
      <path d="M0 4 L6 4 M10 4 L16 4" stroke="#bdbdbd" stroke-width="1"/>
      <path d="M8 1 L10 4 L8 7 L6 4 Z" fill="#f2f2f2"/>
    </svg>
    <p class="tagline">Making each one of your gatherings radiant...</p>
    <div class="rule rule--lower"></div>
  </section>
</main>
</body>
</html>
```